Wedding Invitation Card Design

Design high quality double sided wedding invitation including Monogram, borders matching RSVP cards, Envelope liners and stationary set. Design should be appropriate for printing techniques like gold foiling, edging, letterpress. Size 18 x 12 Rectangle/Horizontal layout.

Preferred color is Gold and matching colors of Gold. Please check attached files for more information.

Target Market(s)

Events

Font styles to use
Serif
Decorative
Script

Colors

Designer to choose colors to be used in the design.

Requirements
Must have
• as described above.
Nice to have
• Excellent borders and monogram.

```html
<!DOCTYPE html>
<html lang="en">
<head>
<meta charset="utf-8">
<title>Wedding Invitation – Clara Rose &amp; Daniel Thomas Avery</title>
<link href="https://fonts.googleapis.com/css2?family=Cinzel:wght@400;600&family=Parisienne&display=swap" rel="stylesheet">
<style>
  :root {
    --backdrop: #8c8c8c;
    --paper: #ece7df;
    --gold-light: #e3b23c;
    --gold: #c88a1c;
    --gold-deep: #9a5a12;
    --gold-gradient: linear-gradient(100deg, #e6b43a 0%, #b9741a 45%, #8f4f10 70%, #d49a2a 100%);
  }
  * { box-sizing: border-box; margin: 0; padding: 0; }
  html, body { width: 848px; height: 1200px; overflow: hidden; }
  body {
    background: var(--backdrop);
    display: flex;
    flex-direction: column;
    align-items: center;
    justify-content: center;
    gap: 60px;
  }
  .card {
    position: relative;
    width: 720px;
    height: 480px;
    background: var(--paper);
    color: var(--gold-deep);
    text-align: center;
  }
  .card__frame {
    position: absolute;
    inset: 0;
    width: 100%;
    height: 100%;
  }
  .card__content {
    position: relative;
    height: 100%;
    display: flex;
    flex-direction: column;
    align-items: center;
  }
  .gold-text {
    background: var(--gold-gradient);
    -webkit-background-clip: text;
    background-clip: text;
    color: transparent;
  }
  .monogram {
    width: 80px;
    height: 56px;
    background: linear-gradient(135deg, var(--gold-light), var(--gold-deep));
    border-radius: 4px;
  }
  .divider { display: block; }
  .invite { padding-top: 64px; }
  .invite .divider { margin: 10px 0 14px; }
  .invite__hosts {
    font-family: "Cinzel", serif;
    font-weight: 600;
    font-size: 15px;
    line-height: 1.2;
  }
  .invite__name {
    font-family: "Parisienne", cursive;
    font-size: 46px;
    line-height: 1.15;
    margin-top: 4px;
  }
  .invite__to {
    font-family: "Cinzel", serif;
    font-weight: 600;
    font-size: 22px;
    margin: 4px 0 0;
  }
  .invite__details {
    font-family: "Cinzel", serif;
    font-weight: 600;
    font-size: 14px;
    line-height: 1.25;
    margin-top: 4px;
  }
  .invite__couple {
    font-family: "Cinzel", serif;
    font-weight: 600;
    font-size: 13px;
    margin-top: 8px;
  }
  .cover { padding-top: 84px; }
  .cover__crest {
    width: 210px;
    height: 180px;
    border-radius: 50% 50% 46% 46%;
    background: radial-gradient(circle at 50% 45%, #b9741a 0%, #d8b77a 45%, #e6dccb 75%, var(--paper) 100%);
  }
  .cover__couple {
    font-family: "Cinzel", serif;
    font-weight: 600;
    font-size: 22px;
    letter-spacing: 0.5px;
    margin-top: 72px;
  }
  .cover .divider { margin: 6px 0 8px; }
  .cover__date {
    font-family: "Cinzel", serif;
    font-size: 15px;
    color: var(--gold);
  }
</style>
</head>
<body>

  <section class="card invite" aria-label="Invitation text side">
    <svg class="card__frame" viewBox="0 0 720 480" aria-hidden="true">
      <defs>
        <linearGradient id="frameGold" x1="0" y1="0" x2="1" y2="1">
          <stop offset="0" stop-color="#e6b43a"/>
          <stop offset="0.5" stop-color="#a9651a"/>
          <stop offset="1" stop-color="#e0aa35"/>
        </linearGradient>
      </defs>
      <rect x="24" y="20" width="672" height="440" fill="none" stroke="url(#frameGold)" stroke-width="2.5"/>
      <rect x="33" y="29" width="654" height="422" fill="none" stroke="url(#frameGold)" stroke-width="1.5"/>
    </svg>
    <div class="card__content">
      <div class="monogram" role="img" aria-label="Gold interlaced couple monogram"></div>
      <svg class="divider" width="220" height="10" viewBox="0 0 220 10" aria-hidden="true">
        <line x1="4" y1="5" x2="216" y2="5" stroke="#c88a1c" stroke-width="1"/>
        <circle cx="4" cy="5" r="2" fill="#c88a1c"/>
        <circle cx="216" cy="5" r="2" fill="#c88a1c"/>
        <path d="M98 5 L110 1 L122 5 L110 9 Z" fill="#c88a1c"/>
      </svg>
      <p class="invite__hosts gold-text">Dr. Helen Marlow and Mr. Robert Marlow<br>request the honor of your presence<br>at the marriage of their daughter</p>
      <p class="invite__name gold-text">Clara Rose</p>
      <p class="invite__to gold-text">to</p>
      <p class="invite__name gold-text">Daniel Thomas Avery</p>
      <p class="invite__details gold-text">on Saturday, the twenty-seventh of November<br>two thousand seventeen<br>at 7 o'clock in the evening</p>
      <p class="invite__couple gold-text">Amara &amp; Niran</p>
    </div>
  </section>

  <section class="card cover" aria-label="Invitation cover side">
    <svg class="card__frame" viewBox="0 0 720 480" aria-hidden="true">
      <defs>
        <linearGradient id="frameGold2" x1="0" y1="0" x2="1" y2="1">
          <stop offset="0" stop-color="#e6b43a"/>
          <stop offset="0.5" stop-color="#a9651a"/>
          <stop offset="1" stop-color="#e0aa35"/>
        </linearGradient>
      </defs>
      <rect x="24" y="20" width="672" height="440" fill="none" stroke="url(#frameGold2)" stroke-width="2.5"/>
      <rect x="33" y="29" width="654" height="422" fill="none" stroke="url(#frameGold2)" stroke-width="1.5"/>
    </svg>
    <div class="card__content">
      <div class="cover__crest" role="img" aria-label="Gold monogram framed by a hand-drawn floral wreath"></div>
      <p class="cover__couple gold-text">Amara &amp; Niran</p>
      <svg class="divider" width="260" height="10" viewBox="0 0 260 10" aria-hidden="true">
        <line x1="4" y1="5" x2="256" y2="5" stroke="#c88a1c" stroke-width="1"/>
        <circle cx="4" cy="5" r="2" fill="#c88a1c"/>
        <circle cx="256" cy="5" r="2" fill="#c88a1c"/>
        <path d="M118 5 L130 1 L142 5 L130 9 Z" fill="#c88a1c"/>
      </svg>
      <p class="cover__date">14 November 2019</p>
    </div>
  </section>

</body>
</html>
```